Brake Test Training for Coal Mining

We offer Brake Test Training for Coal Mine workers. It's a legislative requirement that workers who are tasked with performing brake testing have certain competencies to do so. We test Light Vehicles and trailers, Heavy Vehicles and Mobile Mining Equipment like Graders, Scrapers and Dump Trucks.

```html
<!DOCTYPE html>
<html lang="en">
<head>
<meta charset="utf-8">
<title>Coalface Brake Training – Billboard</title>
<link href="https://fonts.googleapis.com/css2?family=Archivo+Black&family=Open+Sans:wght@400&family=Teko:wght@600&display=swap" rel="stylesheet">
<style>
  :root {
    --navy: #0d3a5c;
    --navy-deep: #14285e;
    --yellow: #f4c20d;
    --white: #ffffff;
    --ink: #111111;
    --stage: #262626;
  }
  html, body {
    margin: 0;
    padding: 0;
    width: 1061px;
    height: 1200px;
    overflow: hidden;
    background: var(--stage);
  }
  .billboard {
    position: absolute;
    left: 30px;
    top: 434px;
    width: 1000px;
    height: 332px;
    box-shadow: 0 18px 30px rgba(0,0,0,0.7);
  }
  .billboard svg { display: block; width: 100%; height: 100%; }
  .brand-name { font-family: "Archivo Black", sans-serif; fill: var(--ink); }
  .brand-tagline { font-family: "Open Sans", sans-serif; fill: var(--ink); }
  .phone { font-family: "Teko", sans-serif; font-weight: 600; fill: var(--white); }
  .web { font-family: "Teko", sans-serif; font-weight: 600; fill: var(--navy); }
</style>
</head>
<body>
<div class="billboard">
  <svg viewBox="0 0 1532 509" xmlns="http://www.w3.org/2000/svg">
    <defs>
      <linearGradient id="haul-truck-tones" x1="0" y1="0" x2="0" y2="1">
        <stop offset="0" stop-color="#8c93a3"/>
        <stop offset="0.45" stop-color="#b39a4a"/>
        <stop offset="1" stop-color="#8a8478"/>
      </linearGradient>
      <linearGradient id="service-ute-tones" x1="0" y1="0" x2="1" y2="1">
        <stop offset="0" stop-color="#ffffff"/>
        <stop offset="1" stop-color="#d9dde2"/>
      </linearGradient>
      <linearGradient id="loader-tones" x1="0" y1="0" x2="0" y2="1">
        <stop offset="0" stop-color="#b7a89a"/>
        <stop offset="0.55" stop-color="#c4a443"/>
        <stop offset="1" stop-color="#a39e95"/>
      </linearGradient>
    </defs>

    <rect class="panel" width="1532" height="509" fill="var(--white)"/>

    <!-- brand block -->
    <circle class="brand-mark" cx="145" cy="160" r="68" fill="var(--navy)"/>
    <line x1="235" y1="106" x2="675" y2="106" stroke="var(--navy-deep)" stroke-width="7"/>
    <text class="brand-name" x="470" y="172" font-size="54" text-anchor="middle" letter-spacing="2">COALFACE</text>
    <text class="brand-tagline" x="470" y="210" font-size="27" text-anchor="middle">BRAKE TEST TRAINING</text>
    <line x1="235" y1="228" x2="675" y2="228" stroke="var(--yellow)" stroke-width="7"/>

    <!-- contact band -->
    <polygon class="band-edge" points="0,300 732,300 832,472 1115,472 1136,509 0,509" fill="var(--yellow)"/>
    <polygon class="contact-band" points="0,309 727,309 826,479 1111,479 1128,509 0,509" fill="var(--navy)"/>
    <text class="phone" x="370" y="408" font-size="112" text-anchor="middle" letter-spacing="4">1300 555 018</text>
    <rect class="web-pill" x="166" y="424" width="406" height="63" rx="6" fill="var(--yellow)"/>
    <text class="web" x="369" y="473" font-size="50" text-anchor="middle" textLength="340" lengthAdjust="spacingAndGlyphs">WWW.CFBT.NET.AU</text>

    <!-- centre hexagon -->
    <polygon class="hex-frame" points="838,0 1104,0 1228,225 1104,452 838,452 706,225" fill="var(--yellow)"/>
    <polygon class="hex-gap" points="842,6 1100,6 1221,225 1100,446 842,446 713,225" fill="var(--white)"/>
    <polygon class="hex-photo" role="img" aria-label="Photo of a large yellow mining haul truck on a gravel site"
      points="848,16 1094,16 1209,225 1094,436 848,436 725,225" fill="url(#haul-truck-tones)"/>

    <!-- top-right cell -->
    <polygon class="cell-edge" points="1112,0 1124,0 1238,212 1532,212 1532,222 1232,222" fill="var(--yellow)"/>
    <polygon class="ute-photo" role="img" aria-label="Photo of a white service ute with a crane on the tray"
      points="1190,10 1532,10 1532,200 1290,200" fill="url(#service-ute-tones)"/>

    <!-- bottom-right cell -->
    <polygon class="cell-edge" points="1236,232 1532,232 1532,242 1248,242 1130,509 1116,509" fill="var(--yellow)"/>
    <polygon class="loader-photo" role="img" aria-label="Photo of a wheel loader filling a mining dump truck"
      points="1252,246 1532,246 1532,509 1136,509" fill="url(#loader-tones)"/>
  </svg>
</div>
</body>
</html>
```